Weight Loss Banner Ad

We need banner ads for our website, www.bluvantaplan.com. We would like to see Banner ads that represent what you think is the most captivating aspect of The Bluvanta Plan. Please review the website.

The banner ad should be something you REALLY want to click on. It needs to include the name and/or logo and the slogan "Gourmet Meals Direct To Your House"

We will want the final ad in multiple sizes but it should use the same image and copy.

Logo is attached, so are images. Feel free to use your own if you think you have a better on

Size (pixels):
468 x 60
392 x 72
234 x 60
125 x 125
120 x 90
120 x 60
88 x 31
120 x 240
120 x 600
160 x 600

Target Market(s)

Fitness Enthusiast looking to lose weight.

Industry/Entity Type

Weight

Font styles to use
Sans Serif

Requirements
Must have
• See Description
Nice to have
• Should be awesome and make you want to buy some food. Also you may want to say something about the price:

i.e. Starting at only $99

```html
<!DOCTYPE html>
<html lang="en">
<head>
<meta charset="utf-8">
<title>Bluvanta Plan – Banner Set</title>
<link rel="stylesheet" href="https://fonts.googleapis.com/css2?family=Open+Sans:wght@700;800&family=Lato:wght@400;700;900&display=swap">
<style>
  :root{
    --page:#ffffff;
    --ink:#262626;
    --band:#414141;
    --lime:#8dc63f;
    --lime-light:#a6dc4e;
    --lime-deep:#4f9a16;
    --white:#ffffff;
    --rule:#b9b9b9;
    --footer:#151515;
    --food-dark:#5b3a26;
    --food-mid:#8a6a4a;
    --food-green:#7aa14a;
    --food-light:#cbbfa3;
  }
  *{box-sizing:border-box;margin:0;padding:0}
  html,body{width:1200px;height:934px;overflow:hidden;background:var(--page)}
  .sheet{position:relative;width:1200px;height:934px}

  .banner{position:absolute;background:var(--ink);border:1px solid var(--rule);overflow:hidden;color:var(--white);font-family:'Lato',sans-serif}

  .brand{background:var(--white);color:var(--lime);font-family:'Lato',sans-serif;font-weight:900;display:flex;flex-direction:column;align-items:center;justify-content:center;line-height:.95;text-align:center;letter-spacing:-.5px}

  .headline{font-family:'Open Sans',sans-serif;font-weight:800;text-transform:uppercase;line-height:1.08;color:var(--white);white-space:nowrap;z-index:2}
  .tagline{color:var(--lime);line-height:1.25;white-space:nowrap;z-index:2}

  .price{display:flex;align-items:center;justify-content:center;background:var(--band);z-index:2}
  .price-lead{color:var(--lime);text-transform:uppercase;line-height:1.1;text-align:center;white-space:nowrap}
  .price-amount{font-family:'Open Sans',sans-serif;font-weight:800;color:var(--white);letter-spacing:-1px;white-space:nowrap}
  .price-amount small{font-size:.5em;font-weight:700;letter-spacing:0}

  .cta{display:flex;align-items:center;justify-content:center;background:linear-gradient(var(--lime-light),var(--lime-deep));border:2px solid var(--white);border-radius:6px;color:#111;font-family:'Lato',sans-serif;font-weight:900;white-space:nowrap;z-index:2}

  .photo{position:absolute;z-index:1;background:linear-gradient(135deg,var(--food-green) 0%,var(--food-mid) 35%,var(--food-dark) 60%,var(--food-light) 100%)}
  .photo svg{position:absolute;display:block}

  .site-url{background:var(--footer);color:var(--white);display:flex;align-items:center;justify-content:center;font-family:'Lato',sans-serif}

  /* 160 x 600 and 120 x 600 */
  .sky-wide{left:39px;top:40px;width:231px;height:848px}
  .sky-narrow{left:291px;top:40px;width:175px;height:848px}
  .sky .brand{position:absolute;left:0;top:0;width:100%;height:123px}
  .sky .headline{position:absolute;left:0;width:100%;text-align:center}
  .sky .tagline{position:absolute;left:0;width:100%;text-align:center}
  .sky .price{position:absolute;left:0;width:100%}
  .sky .cta{position:absolute}
  .sky .photo{left:0;top:500px;width:100%;height:306px}
  .sky .photo svg{left:0;top:-2px;width:100%;height:60px}
  .sky .site-url{position:absolute;left:0;bottom:0;width:100%;height:42px}

  .sky-wide .brand{font-size:40px}
  .sky-wide .headline{top:142px;font-size:32px}
  .sky-wide .tagline{top:290px;font-size:19px}
  .sky-wide .price{top:376px;height:66px;gap:6px}
  .sky-wide .price-lead{font-size:17px}
  .sky-wide .price-amount{font-size:44px}
  .sky-wide .cta{left:22px;top:463px;width:187px;height:42px;font-size:19px}
  .sky-wide .site-url{font-size:19px}

  .sky-narrow .brand{font-size:32px}
  .sky-narrow .headline{top:142px;font-size:23px;line-height:1.3}
  .sky-narrow .tagline{top:285px;font-size:15px}
  .sky-narrow .price{top:376px;height:66px;gap:4px}
  .sky-narrow .price-lead{font-size:13px}
  .sky-narrow .price-amount{font-size:34px}
  .sky-narrow .cta{left:17px;top:463px;width:141px;height:42px;font-size:16px}
  .sky-narrow .site-url{font-size:15px}

  /* 468 x 60 and 392 x 72 */
  .strip .brand{position:absolute;left:0;top:0;height:100%}
  .strip .headline,.strip .tagline,.strip .price{position:absolute}
  .strip .price{gap:6px}
  .strip .photo{right:0;top:0;height:100%}
  .strip .photo svg{left:0;top:0;width:30px;height:100%}

  .leader{left:492px;top:45px;width:678px;height:85px}
  .leader .brand{width:158px;font-size:26px}
  .leader .headline{left:166px;top:6px;font-size:22px}
  .leader .tagline{left:166px;top:62px;font-size:12px}
  .leader .price{left:362px;top:4px;width:170px;height:54px}
  .leader .price-lead{font-size:12px}
  .leader .price-amount{font-size:36px}
  .leader .photo{width:145px}

  .strip-mid{left:492px;top:150px;width:568px;height:103px}
  .strip-mid .brand{width:144px;font-size:26px}
  .strip-mid .headline{left:152px;top:10px;font-size:23px}
  .strip-mid .tagline{left:152px;top:74px;font-size:12.5px}
  .strip-mid .price{left:338px;top:8px;width:160px;height:58px}
  .strip-mid .price-lead{font-size:12px}
  .strip-mid .price-amount{font-size:38px}
  .strip-mid .photo{width:68px}

  /* 234 x 60 */
  .half{left:492px;top:272px;width:340px;height:86px;display:flex}
  .half .brand{width:112px;height:100%;font-size:20px;flex:none}
  .half .copy{width:226px;display:flex;flex-direction:column;justify-content:center;align-items:center}
  .half .headline{font-size:15px;padding:4px 0}
  .half .price{height:46px;width:190px;gap:8px;margin-top:2px}
  .half .price-lead{font-size:12px}
  .half .price-amount{font-size:30px}

  /* boxes */
  .box .brand{position:absolute;left:0;top:0;z-index:2}
  .box .headline,.box .tagline,.box .price,.box .cta{position:absolute}
  .box .price{gap:4px}

  .micro-wide{left:855px;top:272px;width:175px;height:86px}
  .micro-wide .brand{width:95px;height:34px;font-size:14px}
  .micro-wide .headline{left:6px;top:40px;font-size:13px}
  .micro-wide .photo{left:108px;top:0;width:67px;height:100%}
  .micro-wide .photo svg{left:0;top:0;width:22px;height:100%}

  .tower{left:492px;top:381px;width:175px;height:340px}
  .tower .brand{width:100%;height:61px;font-size:24px}
  .tower .headline{left:0;top:67px;width:100%;text-align:center;font-size:20px}
  .tower .tagline{left:0;top:122px;width:100%;text-align:center;font-size:13px}
  .tower .price{left:0;top:170px;width:100%;height:50px}
  .tower .price-lead{font-size:11px}
  .tower .price-amount{font-size:32px}
  .tower .photo{left:0;top:226px;width:100%;height:114px}
  .tower .photo svg{left:0;top:-2px;width:100%;height:30px}
  .tower .cta{left:44px;top:302px;width:124px;height:28px;font-size:12px}

  .square{left:691px;top:381px;width:182px;height:178px}
  .square .brand{width:98px;height:40px;font-size:17px}
  .square .headline{left:6px;top:46px;font-size:14px}
  .square .tagline{left:6px;top:84px;font-size:10px}
  .square .price{left:0;top:116px;width:112px;height:32px}
  .square .price-lead{font-size:8px}
  .square .price-amount{font-size:21px}
  .square .photo{left:116px;top:0;width:66px;height:100%}
  .square .photo svg{left:0;top:0;width:20px;height:100%}
  .square .cta{left:10px;top:153px;width:92px;height:20px;font-size:9.5px;border-width:1px;border-radius:4px}

  .compact{left:889px;top:381px;width:175px;height:128px}
  .compact .brand{width:96px;height:38px;font-size:16px}
  .compact .headline{left:6px;top:44px;font-size:14px}
  .compact .price{left:0;top:84px;width:112px;height:36px}
  .compact .price-lead{font-size:8.5px}
  .compact .price-amount{font-size:23px}
  .compact .photo{left:116px;top:0;width:59px;height:100%}
  .compact .photo svg{left:0;top:0;width:20px;height:100%}

  .button-ad{left:691px;top:578px;width:128px;height:45px;display:flex}
  .button-ad .brand{width:64px;height:100%;font-size:10.5px}
  .button-ad .headline{flex:1;display:flex;align-items:center;justify-content:center;text-align:center;font-size:8px}
</style>
</head>
<body>
<main class="sheet">

  <!-- 160 x 600 -->
  <section class="banner sky sky-wide">
    <div class="brand">Bluvanta<br>Plan</div>
    <h1 class="headline">Effortless<br>Weight<br>Loss</h1>
    <p class="tagline">Gourmet Meal Plans<br>Direct To Your Door</p>
    <div class="price"><span class="price-lead">Starting<br>at only</span><span class="price-amount">$7<small>/meal</small></span></div>
    <div class="photo" role="img" aria-label="Food photo: grilled steak strips, lettuce wraps, roasted vegetables and a bowl of dip on a wooden table">
      <svg viewBox="0 0 231 60" preserveAspectRatio="none"><path d="M0 0H231V8Q120 20 0 60Z" fill="#262626"/><path d="M0 60Q120 20 231 8V16Q120 30 0 60Z" fill="#8dc63f"/></svg>
    </div>
    <a class="cta">LEARN MORE &gt;&gt;</a>
    <div class="site-url">bluvantaplan.com</div>
  </section>

  <!-- 120 x 600 -->
  <section class="banner sky sky-narrow">
    <div class="brand">Bluvanta<br>Plan</div>
    <h1 class="headline">Effortless<br>Weight<br>Loss</h1>
    <p class="tagline">Gourmet Meal Plans<br>Direct To Your Door</p>
    <div class="price"><span class="price-lead">Starting<br>at only</span><span class="price-amount">$7<small>/meal</small></span></div>
    <div class="photo" role="img" aria-label="Food photo: grilled steak strips, lettuce wraps, roasted vegetables and a bowl of dip on a wooden table">
      <svg viewBox="0 0 175 60" preserveAspectRatio="none"><path d="M0 0H175V8Q90 20 0 60Z" fill="#262626"/><path d="M0 60Q90 20 175 8V16Q90 30 0 60Z" fill="#8dc63f"/></svg>
    </div>
    <a class="cta">LEARN MORE &gt;&gt;</a>
    <div class="site-url">bluvantaplan.com</div>
  </section>

  <!-- 468 x 60 -->
  <section class="banner strip leader">
    <div class="brand">Bluvanta<br>Plan</div>
    <h1 class="headline">Effortless<br>Weight Loss</h1>
    <p class="tagline">Gourmet Meal Plans Direct To Your Door</p>
    <div class="price"><span class="price-lead">Starting<br>at only</span><span class="price-amount">$7<small>/meal</small></span></div>
    <div class="photo" role="img" aria-label="Food photo: grilled steak strips with salad and vegetables">
      <svg viewBox="0 0 30 85" preserveAspectRatio="none"><path d="M0 0H12L30 85H0Z" fill="#262626"/><path d="M12 0H18L30 85H24Z" fill="#8dc63f"/></svg>
    </div>
  </section>

  <!-- 392 x 72 -->
  <section class="banner strip strip-mid">
    <div class="brand">Bluvanta<br>Plan</div>
    <h1 class="headline">Effortless<br>Weight Loss</h1>
    <p class="tagline">Gourmet Meal Plans Direct To Your Door</p>
    <div class="price"><span class="price-lead">Starting<br>at only</span><span class="price-amount">$7<small>/meal</small></span></div>
    <div class="photo" role="img" aria-label="Food photo: lettuce wraps and grilled vegetables">
      <svg viewBox="0 0 30 103" preserveAspectRatio="none"><path d="M0 0H12L30 103H0Z" fill="#262626"/><path d="M12 0H18L30 103H24Z" fill="#8dc63f"/></svg>
    </div>
  </section>

  <!-- 234 x 60 -->
  <section class="banner half">
    <div class="brand">Bluvanta<br>Plan</div>
    <div class="copy">
      <h1 class="headline">Effortless Weight Loss</h1>
      <div class="price"><span class="price-lead">Starting<br>at only</span><span class="price-amount">$7<small>/meal</small></span></div>
    </div>
  </section>

  <!-- 120 x 60 -->
  <section class="banner box micro-wide">
    <div class="brand">Bluvanta Plan</div>
    <h1 class="headline">Effortless<br>Weight Loss</h1>
    <div class="photo" role="img" aria-label="Food photo: grilled steak strips and dip">
      <svg viewBox="0 0 22 86" preserveAspectRatio="none"><path d="M0 0H8L22 86H0Z" fill="#262626"/><path d="M8 0H13L22 86H17Z" fill="#8dc63f"/></svg>
    </div>
  </section>

  <!-- 120 x 240 -->
  <section class="banner box tower">
    <div class="brand">Bluvanta<br>Plan</div>
    <h1 class="headline">Effortless<br>Weight Loss</h1>
    <p class="tagline">Gourmet Meal Plans<br>Direct To Your Door</p>
    <div class="price"><span class="price-lead">Starting<br>at only</span><span class="price-amount">$7<small>/meal</small></span></div>
    <div class="photo" role="img" aria-label="Food photo: grilled steak strips, lettuce wraps and roasted vegetables">
      <svg viewBox="0 0 175 30" preserveAspectRatio="none"><path d="M0 0H175V4Q90 10 0 30Z" fill="#262626"/><path d="M0 30Q90 10 175 4V10Q90 18 0 30Z" fill="#8dc63f"/></svg>
    </div>
    <a class="cta">LEARN MORE &gt;&gt;</a>
  </section>

  <!-- 125 x 125 -->
  <section class="banner box square">
    <div class="brand">Bluvanta<br>Plan</div>
    <h1 class="headline">Effortless<br>Weight Loss</h1>
    <p class="tagline">Gourmet Meal Plans<br>Direct To Your Door</p>
    <div class="price"><span class="price-lead">Starting<br>at only</span><span class="price-amount">$7<small>/meal</small></span></div>
    <div class="photo" role="img" aria-label="Food photo: lettuce wraps and grilled steak strips">
      <svg viewBox="0 0 20 178" preserveAspectRatio="none"><path d="M0 0H7L20 178H0Z" fill="#262626"/><path d="M7 0H11L20 178H16Z" fill="#8dc63f"/></svg>
    </div>
    <a class="cta">LEARN MORE &gt;&gt;</a>
  </section>

  <!-- 120 x 90 -->
  <section class="banner box compact">
    <div class="brand">Bluvanta<br>Plan</div>
    <h1 class="headline">Effortless<br>Weight Loss</h1>
    <div class="price"><span class="price-lead">Starting<br>at only</span><span class="price-amount">$7<small>/meal</small></span></div>
    <div class="photo" role="img" aria-label="Food photo: lettuce wraps and grilled steak strips">
      <svg viewBox="0 0 20 128" preserveAspectRatio="none"><path d="M0 0H7L20 128H0Z" fill="#262626"/><path d="M7 0H11L20 128H16Z" fill="#8dc63f"/></svg>
    </div>
  </section>

  <!-- 88 x 31 -->
  <section class="banner button-ad">
    <div class="brand">Bluvanta<br>Plan</div>
    <h1 class="headline">Effortless<br>Weight<br>Loss</h1>
  </section>

</main>
</body>
</html>
```